Web and Logo Design - Investing Website

Financial website, so needs to be clean and professional. I like vector images that are simple and professional (data, investing) but do not overpower the website. Will need to show off the charts to emphasize portfolio’s performance. Should be mainly blue and white (does not have to be the blue tones selected). Homepage should have a section where it shows off the three portfolios with a quick summary (see content file) and performance graph (see performance charts file) - with a "learn more" link.

Homepage Header links - Strategies; Monthly Updates; FAQ; Signup; Login

Pages needed:
Homepage
Articles/Blog Main Page
Article Layout Template
Dashboard Template (see Dashboard information file)

Sample designs i like: https://www.plarvo.io/ - https://www.brisketal.com/ - https://www.halvornquist.com/

Industry/Entity Type

Finance - Investing

Number of Pages Required

4 page

Colors
0054AA
0677BA
7BADD7
CADEEF
E8F1F8

Requirements
Should not have
• Generic pictures of people

```html
<!DOCTYPE html>
<html lang="en">
<head>
<meta charset="utf-8">
<title>Ledgerwise Portfolio – Rules-based investing</title>
<link rel="stylesheet" href="https://fonts.googleapis.com/css2?family=Roboto:wght@400;500;700&display=swap">
<style>
:root{
  --navy:#0054AA;
  --blue:#0677BA;
  --sky:#7BADD7;
  --mist:#CADEEF;
  --ice:#E8F1F8;
  --ink:#111418;
  --text:#3a3f47;
  --bar-a:#8FAEF5;
  --bar-b:#F08A80;
  --white:#fff;
}
*{box-sizing:border-box;margin:0;padding:0}
html,body{width:1200px;height:3286px;overflow:hidden;background:var(--white)}
body{font-family:'Roboto',sans-serif;color:var(--text)}
.page{position:relative;width:1200px;height:3286px;overflow:hidden}
.abs{position:absolute}
a{color:inherit;text-decoration:none}

/* top bar */
.topbar{left:0;top:0;width:1200px;height:56px;background:var(--navy);color:var(--white);font-size:13px}
.topbar .pill{position:absolute;left:109px;top:15px;height:26px;padding:0 20px;border-radius:13px;background:var(--white);color:var(--navy);font-size:10px;line-height:26px}
.topbar .promo{position:absolute;left:237px;top:20px;font-size:12px}
.topbar .util{position:absolute;right:100px;top:20px;display:flex;gap:40px;font-size:13px}

/* nav */
.brand{left:106px;top:83px;height:40px;display:flex;align-items:center;gap:8px;font-size:21px;color:var(--navy);letter-spacing:.3px}
.brand .mark{width:10px;height:10px;background:var(--navy)}
.mainnav{left:524px;top:92px;display:flex;gap:37px;font-size:14px;color:var(--ink)}
.btn-outline{left:838px;top:80px;width:126px;height:44px;border:1px solid var(--navy);border-radius:22px;color:var(--navy);font-size:15px;display:flex;align-items:center;justify-content:center}
.btn-solid{left:974px;top:80px;width:124px;height:43px;border-radius:22px;background:var(--navy);color:var(--white);font-size:15px;display:flex;align-items:center;justify-content:center}

/* hero */
.hero-bg{left:0;top:140px;width:1200px;height:540px}
.hero-title{left:98px;top:242px;font-size:47px;font-weight:700;line-height:54px;color:var(--ink)}
.hero-title span{color:var(--blue)}
.btn{border-radius:22px;background:var(--navy);color:var(--white);font-size:15px;display:flex;align-items:center;justify-content:center}
.hero-cta{left:101px;top:431px;width:144px;height:43px}
.hero-art{left:590px;top:172px;width:540px;height:440px;background:radial-gradient(closest-side at 55% 50%,#2d8fe0 0%,#7BADD7 45%,rgba(202,222,239,.5) 75%,rgba(232,241,248,0) 100%)}

/* about */
.about{left:137px;top:732px;width:926px;height:213px;background:var(--white);box-shadow:0 4px 18px rgba(0,60,120,.08);text-align:center;padding-top:40px}
.about h2{font-size:31px;font-weight:700;color:var(--navy);margin-bottom:8px}
.about p{font-size:17px;line-height:31px;color:var(--text);padding:0 28px}

/* section titles */
.sec-title{left:0;width:1200px;text-align:center;font-size:38px;font-weight:700;color:var(--ink)}
.sec-title span{color:var(--blue)}
.sec-rule{width:54px;height:2px;background:var(--navy);left:573px}

/* portfolios */
.chart-card{width:450px;height:318px;background:var(--white);box-shadow:0 2px 12px rgba(0,40,90,.18)}
.dots-pattern{width:145px;height:150px;background-image:radial-gradient(#c9d3df 1.1px,transparent 1.2px);background-size:8px 8px}
.pf-title{font-size:38px;font-weight:700;color:var(--ink)}
.pf-title span{color:var(--blue)}
.pf-text{font-size:17px;line-height:32.5px;letter-spacing:.15px;color:var(--text);width:462px}
.pf-btn{width:144px;height:42px}

/* included */
.included-bg{left:0;top:2505px;width:1200px;height:480px;background:var(--ice)}
.feature{width:200px;text-align:center;font-size:20px;font-weight:500;color:var(--ink);line-height:23px}
.feature .ico{width:98px;height:98px;border-radius:50%;background:var(--mist);margin:0 auto 22px;display:flex;align-items:center;justify-content:center}
.divider{width:1px;height:118px;background:#d5e0ea;top:2698px}

/* footer */
.footer-bg{left:0;top:2890px;width:1200px;height:396px}
.f-col{color:var(--white);font-size:13px;line-height:25.5px}
.f-col h4{font-size:17px;font-weight:700;margin-bottom:10px;position:relative;line-height:22px}
.f-col h4::after{content:"";position:absolute;left:0;bottom:-6px;width:26px;height:2px;background:var(--white)}
.socials{display:flex;gap:8px;margin-top:14px}
.socials i{width:29px;height:29px;border-radius:50%;border:1.5px solid var(--white);background:rgba(255,255,255,.12)}
.f-cta{left:834px;top:2993px;color:var(--white);font-size:20px;font-weight:700;line-height:31px}
.f-btn{left:834px;top:3100px;width:145px;height:47px;border:1.5px solid var(--white);border-radius:24px;color:var(--white);font-size:17px;display:flex;align-items:center;justify-content:center}
.to-top{left:1115px;top:3166px;width:38px;height:38px;border-radius:50%;background:rgba(0,40,110,.6)}
.f-rule{left:104px;top:3220px;width:978px;height:1px;background:rgba(255,255,255,.45)}
.copy{top:3240px;color:var(--white);font-size:13px}
</style>
</head>
<body>
<div class="page">

  <!-- top bar -->
  <div class="abs topbar">
    <span class="pill">WATCH DEMOS</span>
    <span class="promo">Watch demo videos for popular Brisketal use cases</span>
    <nav class="util">
      <a href="#"><svg width="15" height="15" viewBox="0 0 16 16" style="vertical-align:-2px;margin-right:6px"><circle cx="6.5" cy="6.5" r="5" fill="none" stroke="#fff" stroke-width="1.5"/><line x1="10.3" y1="10.3" x2="14.5" y2="14.5" stroke="#fff" stroke-width="1.5"/></svg>SEARCH</a>
      <a href="#">CONTACT SALES</a>
      <a href="#">CAREERS</a>
      <a href="#">LOG IN</a>
    </nav>
  </div>

  <!-- hero background -->
  <svg class="abs hero-bg" viewBox="0 0 1200 540" preserveAspectRatio="none">
    <defs><linearGradient id="heroGrad" x1="0" y1="0" x2="0" y2="1"><stop offset="0" stop-color="#ffffff"/><stop offset="1" stop-color="#E8F1F8"/></linearGradient></defs>
    <path d="M0 0H1200V440C1080 500 960 520 820 490C660 455 520 395 330 450C200 488 100 470 0 430Z" fill="url(#heroGrad)"/>
  </svg>

  <!-- header -->
  <a class="abs brand" href="#"><span class="mark"></span>LEDGERWISE PORTFOLIO</a>
  <nav class="abs mainnav"><a href="#">Strategies</a><a href="#">Monthly Updates</a><a href="#">FAQ</a></nav>
  <a class="abs btn-outline" href="#">Get In Touch</a>
  <a class="abs btn-solid" href="#">Sign Up</a>

  <!-- hero -->
  <h1 class="abs hero-title">Rules-based investing<br>strategies <span>using<br>quantitative analysis</span></h1>
  <a class="abs btn hero-cta" href="#">Get Started</a>
  <div class="abs hero-art" role="img" aria-label="Isometric illustration of a laptop with data dashboards, servers and a smartphone connected by circuit lines"></div>

  <!-- about -->
  <section class="abs about">
    <h2>LEDGERWISE PORTFOLIO</h2>
    <p>LedgerwisePortfolio.com uses market data, factoring and backtesting to make data driven investment decisions and help craft portfolios that have a high probability of beating the market over the long term. Our algorithms provide rules based investment strategies that investors trade in their own accounts.</p>
  </section>

  <!-- portfolios -->
  <h2 class="abs sec-title" style="top:1022px">Our <span>Portfolios</span></h2>
  <div class="abs sec-rule" style="top:1077px"></div>

  <!-- connectors -->
  <svg class="abs" style="left:0;top:0" width="1200" height="2100" viewBox="0 0 1200 2100">
    <path d="M440 1460V1510Q440 1525 455 1525H710Q725 1525 725 1540V1598" fill="none" stroke="var(--navy)" stroke-width="1.5"/>
    <path d="M725 1935V1985Q725 2000 710 2000H455Q440 2000 440 2015V2077" fill="none" stroke="var(--navy)" stroke-width="1.5"/>
  </svg>

  <!-- portfolio 1 -->
  <div class="abs dots-pattern" style="left:104px;top:1320px"></div>
  <figure class="abs chart-card" style="left:138px;top:1127px">
    <svg width="450" height="318" viewBox="0 0 450 318" font-family="Roboto,sans-serif">
      <circle cx="22" cy="23" r="5" fill="#7BADD7"/><circle cx="38" cy="23" r="5" fill="#7BADD7"/><circle cx="54" cy="23" r="5" fill="#7BADD7"/>
      <line x1="0" y1="43" x2="450" y2="43" stroke="#7BADD7" stroke-width="2"/>
      <text x="225" y="64" font-size="12" fill="#555" text-anchor="middle">Conservative ETF Rotation</text>
      <g stroke="#e3e3e3" stroke-width=".7">
        <line x1="52" y1="80" x2="445" y2="80"/><line x1="52" y1="101" x2="445" y2="101"/><line x1="52" y1="123" x2="445" y2="123"/><line x1="52" y1="144" x2="445" y2="144"/><line x1="52" y1="165" x2="445" y2="165"/><line x1="52" y1="186" x2="445" y2="186"/><line x1="52" y1="208" x2="445" y2="208"/><line x1="52" y1="229" x2="445" y2="229"/><line x1="52" y1="250" x2="445" y2="250" stroke="#bbb"/>
      </g>
      <g font-size="8" fill="#666" text-anchor="end">
        <text x="46" y="83">160.00%</text><text x="46" y="104">140.00%</text><text x="46" y="126">120.00%</text><text x="46" y="147">100.00%</text><text x="46" y="168">80.00%</text><text x="46" y="189">60.00%</text><text x="46" y="211">40.00%</text><text x="46" y="232">20.00%</text><text x="46" y="253">0.00%</text>
      </g>
      <g fill="var(--bar-a)"><rect x="68" y="227" width="30" height="23"/><rect x="165" y="219" width="30" height="31"/><rect x="262" y="151" width="30" height="99"/><rect x="359" y="107" width="30" height="143"/></g>
      <g fill="var(--bar-b)"><rect x="102" y="245" width="30" height="5"/><rect x="199" y="242" width="30" height="8"/><rect x="296" y="215" width="30" height="35"/><rect x="393" y="192" width="30" height="58"/></g>
      <g font-size="8" fill="#777" text-anchor="middle">
        <text x="83" y="223">21.56%</text><text x="117" y="241">4.49%</text><text x="180" y="215">28.90%</text><text x="214" y="238">7.43%</text><text x="277" y="147">93.38%</text><text x="311" y="211">33.05%</text><text x="374" y="103">134.62%</text><text x="408" y="188">54.30%</text>
        <text x="100" y="264">YTD Return</text><text x="197" y="264">1yr Return</text><text x="294" y="264">3yr Return</text><text x="391" y="264">5yr Return</text>
      </g>
      <rect x="135" y="299" width="5" height="5" fill="var(--bar-a)"/><text x="142" y="304" font-size="7.5" fill="#777">Quant 60/40</text>
      <rect x="200" y="299" width="5" height="5" fill="var(--bar-b)"/><text x="207" y="304" font-size="7.5" fill="#777">All World 60/40 (Benchmark)</text>
    </svg>
  </figure>
  <h3 class="abs pf-title" style="left:635px;top:1122px">Conservative ETF <span>Rotation</span></h3>
  <p class="abs pf-text" style="left:636px;top:1185px">Holds 2 ETFs and are rotated and/or rebalanced on the last trading day of the month. Holds a 60% Equity and 40% Bond allocation. It switches its equity allocation to cash when volatility comes into the market. It is backtested to beat a 60/40 portfolio and keep up with the Benchmark 500 with less drawdowns and volatility.</p>
  <a class="abs btn pf-btn" style="left:636px;top:1400px" href="#">Learn More</a>

  <!-- portfolio 2 -->
  <h3 class="abs pf-title" style="left:106px;top:1597px">Growth ETF <span>Rotation</span></h3>
  <p class="abs pf-text" style="left:107px;top:1660px">Holds 4 ETFs and are rotated and/or rebalanced on the last trading day of the month. The strategy holds the strongest sectors. The allocation will sometimes be a full equity allocation, and sometimes have a bond allocation. This strategy is back-tested to beat the market long term with less volatility.</p>
  <a class="abs btn pf-btn" style="left:107px;top:1875px" href="#">Learn More</a>
  <div class="abs dots-pattern" style="left:948px;top:1793px"></div>
  <figure class="abs chart-card" style="left:610px;top:1602px">
    <svg width="450" height="318" viewBox="0 0 450 318" font-family="Roboto,sans-serif">
      <circle cx="28" cy="23" r="5" fill="#7BADD7"/><circle cx="44" cy="23" r="5" fill="#7BADD7"/><circle cx="60" cy="23" r="5" fill="#7BADD7"/>
      <line x1="0" y1="43" x2="450" y2="43" stroke="#7BADD7" stroke-width="2"/>
      <text x="6" y="70" font-size="12" fill="#555">Growth ETF Rotation</text>
      <g stroke="#e3e3e3" stroke-width=".7">
        <line x1="52" y1="80" x2="445" y2="80"/><line x1="52" y1="108" x2="445" y2="108"/><line x1="52" y1="137" x2="445" y2="137"/><line x1="52" y1="165" x2="445" y2="165"/><line x1="52" y1="193" x2="445" y2="193"/><line x1="52" y1="222" x2="445" y2="222"/><line x1="52" y1="250" x2="445" y2="250" stroke="#bbb"/>
      </g>
      <g font-size="8" fill="#666" text-anchor="end">
        <text x="46" y="83">300.00%</text><text x="46" y="111">250.00%</text><text x="46" y="140">200.00%</text><text x="46" y="168">150.00%</text><text x="46" y="196">100.00%</text><text x="46" y="225">50.00%</text><text x="46" y="253">0.00%</text>
      </g>
      <g fill="var(--bar-a)"><rect x="68" y="238" width="30" height="12"/><rect x="165" y="231" width="30" height="19"/><rect x="262" y="175" width="30" height="75"/><rect x="359" y="88" width="30" height="162"/></g>
      <g fill="var(--bar-b)"><rect x="102" y="241" width="30" height="9"/><rect x="199" y="236" width="30" height="14"/><rect x="296" y="218" width="30" height="32"/><rect x="393" y="183" width="30" height="67"/></g>
      <g font-size="8" fill="#777" text-anchor="middle">
        <text x="83" y="234">21.42%</text><text x="117" y="237">15.92%</text><text x="180" y="227">33.33%</text><text x="214" y="232">25.12%</text><text x="277" y="171">132.37%</text><text x="311" y="214">56.66%</text><text x="374" y="84">284.95%</text><text x="408" y="179">117.49%</text>
        <text x="100" y="264">YTD Return</text><text x="197" y="264">1yr Return</text><text x="294" y="264">3yr Return</text><text x="391" y="264">5yr Return</text>
      </g>
      <rect x="175" y="299" width="5" height="5" fill="var(--bar-a)"/><text x="182" y="304" font-size="7.5" fill="#777">Quant Rotation</text>
      <rect x="245" y="299" width="5" height="5" fill="var(--bar-b)"/><text x="252" y="304" font-size="7.5" fill="#777">BMK</text>
    </svg>
  </figure>

  <!-- portfolio 3 -->
  <div class="abs dots-pattern" style="left:104px;top:2270px"></div>
  <figure class="abs chart-card" style="left:138px;top:2077px">
    <svg width="450" height="318" viewBox="0 0 450 318" font-family="Roboto,sans-serif">
      <circle cx="22" cy="23" r="5" fill="#7BADD7"/><circle cx="38" cy="23" r="5" fill="#7BADD7"/><circle cx="54" cy="23" r="5" fill="#7BADD7"/>
      <line x1="0" y1="43" x2="450" y2="43" stroke="#7BADD7" stroke-width="2"/>
      <text x="222" y="64" font-size="12" fill="#555" text-anchor="middle">Whale Rotation</text>
      <g stroke="#e3e3e3" stroke-width=".7">
        <line x1="52" y1="80" x2="445" y2="80"/><line x1="52" y1="99" x2="445" y2="99"/><line x1="52" y1="118" x2="445" y2="118"/><line x1="52" y1="137" x2="445" y2="137"/><line x1="52" y1="156" x2="445" y2="156"/><line x1="52" y1="175" x2="445" y2="175"/><line x1="52" y1="194" x2="445" y2="194"/><line x1="52" y1="212" x2="445" y2="212"/><line x1="52" y1="231" x2="445" y2="231"/><line x1="52" y1="250" x2="445" y2="250" stroke="#bbb"/>
      </g>
      <g font-size="8" fill="#666" text-anchor="end">
        <text x="46" y="83">180.00%</text><text x="46" y="102">160.00%</text><text x="46" y="121">140.00%</text><text x="46" y="140">120.00%</text><text x="46" y="159">100.00%</text><text x="46" y="178">80.00%</text><text x="46" y="197">60.00%</text><text x="46" y="215">40.00%</text><text x="46" y="234">20.00%</text><text x="46" y="253">0.00%</text>
      </g>
      <g fill="var(--bar-a)"><rect x="68" y="241" width="30" height="9"/><rect x="165" y="219" width="30" height="31"/><rect x="262" y="180" width="30" height="70"/><rect x="359" y="105" width="30" height="145"/></g>
      <g fill="var(--bar-b)"><rect x="102" y="238" width="30" height="12"/><rect x="199" y="212" width="30" height="38"/><rect x="296" y="191" width="30" height="59"/><rect x="393" y="138" width="30" height="112"/></g>
      <g font-size="8" fill="#777" text-anchor="middle">
        <text x="83" y="237">9.68%</text><text x="117" y="234">12.38%</text><text x="180" y="215">32.50%</text><text x="214" y="208">39.85%</text><text x="277" y="176">74.09%</text><text x="311" y="187">62.52%</text><text x="374" y="101">153.75%</text><text x="408" y="134">118.81%</text>
        <text x="100" y="264">YTD Return</text><text x="197" y="264">1yr Return</text><text x="294" y="264">3yr Return</text><text x="391" y="264">5yr Return</text>
      </g>
      <rect x="167" y="299" width="5" height="5" fill="var(--bar-a)"/><text x="174" y="304" font-size="7.5" fill="#777">Whale Rotation</text>
      <rect x="240" y="299" width="5" height="5" fill="var(--bar-b)"/><text x="247" y="304" font-size="7.5" fill="#777">Benchmark 500</text>
    </svg>
  </figure>
  <h3 class="abs pf-title" style="left:635px;top:2090px">Whale <span>Rotation</span></h3>
  <p class="abs pf-text" style="left:636px;top:2152px">Holds 4 large cap stocks and are rotated and/or rebalanced on the last trading day of the month. This will always have a 100% equity allocation, so the volatility and drawdowns will be larger. This strategy has shown to beat the market significantly over the mid to long term.</p>
  <a class="abs btn pf-btn" style="left:636px;top:2338px" href="#">Learn More</a>

  <!-- what's included -->
  <div class="abs included-bg"></div>
  <h2 class="abs sec-title" style="top:2572px">What's <span>Included</span></h2>
  <div class="abs sec-rule" style="top:2627px"></div>

  <div class="abs feature" style="left:126px;top:2685px">
    <div class="ico"><svg width="44" height="50" viewBox="0 0 44 50" fill="none" stroke="var(--navy)" stroke-width="2"><rect x="6" y="4" width="32" height="42" rx="2"/><rect x="12" y="14" width="20" height="12"/><line x1="12" y1="32" x2="32" y2="32"/><line x1="12" y1="38" x2="26" y2="38"/></svg></div>
    Updates To All<br>Portfolios
  </div>
  <div class="abs divider" style="left:364px"></div>
  <div class="abs feature" style="left:390px;top:2685px">
    <div class="ico"><svg width="56" height="56" viewBox="0 0 56 56" fill="none" stroke="var(--navy)" stroke-width="2"><path d="M28 4l6 6h8v8l6 6-6 6v8h-8l-6 6-6-6h-8v-8l-6-6 6-6v-8h8z"/><circle cx="28" cy="28" r="12"/></svg></div>
    14 Day Free<br>Trial
  </div>
  <div class="abs divider" style="left:617px"></div>
  <div class="abs feature" style="left:641px;top:2682px">
    <div class="ico"><svg width="44" height="50" viewBox="0 0 44 50" fill="none" stroke="var(--navy)" stroke-width="2"><path d="M6 4h22l8 8v20"/><path d="M6 4v42h20"/><line x1="12" y1="18" x2="28" y2="18"/><line x1="12" y1="24" x2="28" y2="24"/><line x1="12" y1="30" x2="24" y2="30"/><path d="M30 36l10 10M40 36l-10 10"/></svg></div>
    Cancel<br>Anytime
  </div>
  <div class="abs divider" style="left:864px"></div>
  <div class="abs feature" style="left:888px;top:2695px">
    <div class="ico"><svg width="52" height="46" viewBox="0 0 52 46" fill="none" stroke="var(--navy)" stroke-width="2"><rect x="16" y="4" width="32" height="22" rx="2"/><circle cx="32" cy="15" r="5"/><rect x="8" y="14" width="24" height="26" rx="2"/><line x1="14" y1="24" x2="26" y2="24"/><line x1="14" y1="30" x2="22" y2="30"/></svg></div>
    $14.95/M
  </div>

  <!-- footer -->
  <svg class="abs footer-bg" viewBox="0 0 1200 396" preserveAspectRatio="none">
    <defs><linearGradient id="footGrad" x1="0" y1="0" x2="1" y2="1"><stop offset="0" stop-color="#0a5fb8"/><stop offset="1" stop-color="#0048a0"/></linearGradient></defs>
    <path d="M0 44C180 4 360 80 620 50C860 22 1020 -10 1200 18V396H0Z" fill="url(#footGrad)"/>
  </svg>

  <div class="abs f-col" style="left:104px;top:3002px;width:272px">
    <h4>Company</h4>
    <p style="margin-top:14px">Sed ut perspiciatis unde omnis iste natus error sit voluptatem accusaum doloremque laudantium, totam rem aperiam, eaque ipsa</p>
    <div class="socials"><i></i><i></i><i></i><i></i></div>
  </div>
  <div class="abs f-col" style="left:455px;top:3002px">
    <h4>Links</h4>
    <ul style="list-style:none;margin-top:14px"><li>&nbsp;Strategies</li><li>Monthly Updates</li><li>FAQ</li><li>Contact Us</li></ul>
  </div>
  <div class="abs f-col" style="left:638px;top:3002px">
    <h4>Other Links</h4>
    <ul style="list-style:none;margin-top:14px"><li>Legal</li><li>Our Product</li><li>Terms and<br>conditions</li><li>Privacy Policy</li></ul>
  </div>
  <p class="abs f-cta">Take your Business to<br>the next level with<br>Ledgerwise Portfolio</p>
  <a class="abs f-btn" href="#">Get a Quote</a>
  <a class="abs to-top" href="#" aria-label="Back to top"><svg width="38" height="38" viewBox="0 0 38 38" fill="none" stroke="#fff" stroke-width="1.5"><path d="M15 20l4-4 4 4M15 24l4-4 4 4"/></svg></a>
  <div class="abs f-rule"></div>
  <p class="abs copy" style="left:106px">© Copyright 2021 Ledgerwise Portfolio. All Rights Reserved.</p>
  <p class="abs copy" style="right:100px">Terms and Conditions. Privacy Policy.</p>

</div>
</body>
</html>
```